new roofing company card

New primary business card for roofing company.

Industry/Entity Type

Residential roofing/Specializing in Asphalt and Standing seam metal roofing

Contact Information for Business Card

Phone number is: 484 672 1058 Email: support@fennridgeroofworks.com website: www.fennridgeroofworks.com

Colors
EB3D1F
EC4F4E
F09395
F8D3D4
FCEDEE

```html
<!DOCTYPE html>
<html lang="en">
<head>
<meta charset="utf-8">
<title>Fennridge Roofworks – Business Card</title>
<link rel="stylesheet" href="https://fonts.googleapis.com/css2?family=Cinzel:wght@400&family=Open+Sans:wght@400;700&display=swap">
<style>
  :root {
    --backdrop: #989898;
    --brand-red: #c0302a;
    --brand-red-soft: #d2443c;
    --charcoal: #272927;
    --paper: #ffffff;
    --ink: #111111;
    --muted: #6f6f6f;
  }
  * { box-sizing: border-box; margin: 0; padding: 0; }
  html, body { width: 1200px; height: 1000px; overflow: hidden; }
  body {
    background: var(--backdrop);
    font-family: "Open Sans", Arial, sans-serif;
    position: relative;
  }
  .card {
    position: absolute;
    left: 275px;
    width: 650px;
    height: 372px;
    border-radius: 26px;
    overflow: hidden;
  }
  .card--front {
    top: 90px;
    background: var(--brand-red);
    color: var(--paper);
    text-align: center;
  }
  .wordmark {
    position: absolute;
    left: 0; right: 0;
    top: 118px;
    font-family: "Cinzel", Georgia, serif;
    font-weight: 400;
    color: var(--paper);
  }
  .wordmark__name {
    display: block;
    font-size: 50px;
    line-height: 1;
    letter-spacing: 1px;
  }
  .wordmark__tagline {
    display: flex;
    align-items: center;
    justify-content: center;
    gap: 8px;
    margin-top: 10px;
    font-size: 18px;
    letter-spacing: 0.5px;
  }
  .wordmark__rule {
    width: 18px;
    height: 2px;
    background: var(--paper);
  }
  .front-url {
    position: absolute;
    left: 0; right: 0;
    top: 292px;
    font-size: 15px;
    letter-spacing: 0.2px;
  }
  .card--back {
    top: 482px;
    background: var(--paper);
  }
  .brand-mark-area {
    position: absolute;
    left: 250px;
    top: 68px;
    right: 0;
    bottom: 0;
    background: linear-gradient(160deg, var(--brand-red-soft) 0%, var(--brand-red) 55%, var(--charcoal) 100%);
    clip-path: polygon(42% 0, 100% 0, 100% 100%, 0 100%);
  }
  .contact {
    position: absolute;
    left: 30px;
    width: 260px;
    top: 143px;
    text-align: center;
  }
  .contact__name {
    color: var(--brand-red);
    font-weight: 700;
    font-size: 20px;
    line-height: 1.1;
  }
  .contact__title {
    color: var(--ink);
    font-size: 19px;
    line-height: 1.2;
  }
  .contact__icons {
    display: flex;
    justify-content: center;
    gap: 12px;
    margin: 12px 0 10px;
  }
  .contact__icons svg { width: 20px; height: 20px; fill: var(--brand-red); }
  .contact__lines {
    list-style: none;
    color: var(--muted);
    font-size: 13.5px;
    line-height: 17px;
  }
</style>
</head>
<body>

<section class="card card--front">
  <div class="wordmark">
    <span class="wordmark__name">FENNRIDGE</span>
    <span class="wordmark__tagline"><span class="wordmark__rule"></span>ROOFWORKS<span class="wordmark__rule"></span></span>
  </div>
  <p class="front-url">www.fennridgeroofworks.com</p>
</section>

<section class="card card--back">
  <div class="brand-mark-area" role="img" aria-label="Large brand mark in red and charcoal"></div>
  <div class="contact">
    <h1 class="contact__name">NAME SURNAME</h1>
    <p class="contact__title">TITLE</p>
    <div class="contact__icons">
      <svg viewBox="0 0 20 20" aria-hidden="true"><rect x="5" y="1" width="10" height="18" rx="2"/><circle cx="10" cy="16" r="1" fill="#fff"/></svg>
      <svg viewBox="0 0 20 20" aria-hidden="true"><rect x="1" y="4" width="18" height="12"/><path d="M1.5 4.5 L10 11 L18.5 4.5" stroke="#fff" stroke-width="1.2" fill="none"/><path d="M1.5 15.5 L7.5 9.5 M18.5 15.5 L12.5 9.5" stroke="#fff" stroke-width="1" fill="none"/></svg>
      <svg viewBox="0 0 20 20" aria-hidden="true"><circle cx="10" cy="10" r="9"/><g stroke="#fff" stroke-width="1" fill="none"><ellipse cx="10" cy="10" rx="4" ry="9"/><line x1="10" y1="1" x2="10" y2="19"/><line x1="1" y1="10" x2="19" y2="10"/><line x1="2.5" y1="5.5" x2="17.5" y2="5.5"/><line x1="2.5" y1="14.5" x2="17.5" y2="14.5"/></g></svg>
    </div>
    <ul class="contact__lines">
      <li>484 672 1058</li>
      <li>support@fennridgeroofworks.com</li>
      <li>www.fennridgeroofworks.com</li>
    </ul>
  </div>
</section>

</body>
</html>
```